Pritchard's carpentry business card

We need a business card design for Pritchard's Carpentry. A draft has been attached. We already have a logo, however can this please be corrected to include an apostrophe (from "Pritchards Carpentry" to "Pritchard's Carpentry). We would also like the background colour of the logo to be electric blue to match the rest of the business card. We would like the card to be simple, our services are aimed at residential home owners and agricultural business owners. The card can be either single or two-sided, if two sided we would prefer the logo to be one side of the card. Once completed we would like a copy of our logo with the apostrophe on white background as a high resolution image file, as well as a copy with blue background, and a high resolution copy our the image file for our business card. Thank you :)

Carpentry

```html
<!DOCTYPE html>
<html lang="en">
<head>
<meta charset="utf-8">
<title>Pritchard's Carpentry – Business Card</title>
<link rel="stylesheet" href="https://fonts.googleapis.com/css2?family=Alegreya:wght@400;500&display=swap">
<style>
  :root {
    --page: #ffffff;
    --card-blue: #3355ff;
    --text-white: #ffffff;
    --text-dark: #0a0a1a;
    --accent-orange: #ff8a2a;
  }
  * { margin: 0; padding: 0; box-sizing: border-box; }
  html, body {
    width: 1200px; height: 900px; overflow: hidden;
    background: var(--page);
    font-family: "Alegreya", Georgia, serif;
  }
  .business-card {
    position: absolute; left: 253px; top: 251px;
    width: 647px; height: 336px;
    background: var(--card-blue);
  }
  .brand {
    position: absolute; left: 12px; top: 8px;
    width: 278px; height: 228px;
    display: flex; align-items: center; justify-content: center; gap: 12px;
  }
  .brand-dot { width: 34px; height: 34px; border-radius: 50%; background: var(--text-white); flex: none; }
  .brand-name { color: var(--text-white); font-size: 30px; font-weight: 500; line-height: 1.1; }
  .services {
    position: absolute; left: 14px; top: 236px;
    list-style: none; color: var(--text-white); font-size: 15.5px;
  }
  .services li { height: 35.5px; display: flex; align-items: flex-start; gap: 8px; }
  .services li::before {
    content: ""; width: 4px; height: 4px; background: var(--text-white);
    margin-top: 9px; flex: none;
  }
  .owner-name {
    position: absolute; left: 325px; top: 4px;
    color: var(--accent-orange); font-size: 31px; font-weight: 400; letter-spacing: 0.5px;
  }
  .owner-title {
    position: absolute; left: 325px; top: 35px;
    color: var(--text-white); font-size: 15.5px;
  }
  .contact-row { position: absolute; left: 322px; font-size: 15.5px; display: flex; }
  .contact-label { width: 98px; color: var(--text-dark); }
  .contact-value { color: var(--text-white); line-height: 1.05; }
  .contact-value.email { color: var(--accent-orange); }
  .insurance {
    position: absolute; left: 324px; top: 306px;
    color: var(--text-dark); font-size: 15.5px;
  }
</style>
</head>
<body>
  <section class="business-card">
    <div class="brand">
      <span class="brand-dot"></span>
      <span class="brand-name">Pritchard's Carpentry</span>
    </div>

    <ul class="services">
      <li>Restorations &amp; Renovations</li>
      <li>Private, Agricultural &amp; Commercial</li>
      <li>No job too big or small</li>
    </ul>

    <h1 class="owner-name">DANIEL PRITCHARD</h1>
    <p class="owner-title">Qualified carpenter, 10+ years experience</p>

    <div class="contact-row" style="top:78px"><span class="contact-label">Phone:</span><span class="contact-value">0400 555 019</span></div>
    <div class="contact-row" style="top:118px"><span class="contact-label">Address:</span><span class="contact-value">112 Kestrel Creek Road,<br>Brindlewood QLD 4861</span></div>
    <div class="contact-row" style="top:173px"><span class="contact-label">Email:</span><span class="contact-value email">danpritchard@example.com</span></div>
    <div class="contact-row" style="top:219px"><span class="contact-label">ABN:</span><span class="contact-value">12 345 678 901</span></div>
    <div class="contact-row" style="top:259px"><span class="contact-label">BSA lic No:</span><span class="contact-value">1234567</span></div>

    <p class="insurance">Fully insured by Allied Builders</p>
  </section>
</body>
</html>
```